Security Warning Sign

We have an existing sign that needs an update. I have attached a picture of the current square sign. We need to maintain the same wording. It needs to be professional and appropriate to attach to our customers fence. Also attached is a copy of our building sign which may lend some inspiration and hopefully the ai format will assist. The final sign will be 600mm x 600mmOur website is www.harbourlinewatch.com.au

```html
<!DOCTYPE html>
<html lang="en">
<head>
<meta charset="utf-8">
<title>Security Warning Sign – Harbourline Watch Services</title>
<link href="https://fonts.googleapis.com/css2?family=Roboto:wght@700;900&display=swap" rel="stylesheet">
<style>
  :root {
    --sign-yellow: #f0fc0c;
    --tape-gold: #f2b52c;
    --ink: #000000;
    --paper: #ffffff;
    --brand-orange: #f48220;
    --muted-grey: #3a3a3a;
  }
  * { margin: 0; padding: 0; box-sizing: border-box; }
  html, body {
    width: 1200px; height: 1100px; overflow: hidden;
    background: var(--paper);
    font-family: "Roboto", Arial, sans-serif;
  }
  .sign {
    position: absolute; left: 28px; top: 40px;
    width: 1144px; height: 1020px;
    background: var(--sign-yellow);
    border: 5px solid var(--ink);
    border-radius: 10px;
    overflow: hidden;
  }
  .tape { position: absolute; left: 0; width: 100%; height: 70px; display: block; }
  .tape--top { top: 0; }
  .tape--bottom { bottom: 0; }
  .tape-text {
    font-family: "Roboto", Arial, sans-serif;
    font-weight: 700; font-size: 17px; fill: var(--ink);
  }
  .headline-box {
    position: absolute; left: 67px; top: 98px;
    width: 996px; height: 249px;
    background: var(--ink); border-radius: 8px;
    display: flex; align-items: center; justify-content: center;
  }
  .headline {
    color: var(--paper); font-weight: 900;
    font-size: 198px; letter-spacing: 2px; line-height: 1;
    padding-top: 6px;
  }
  .notice {
    position: absolute; left: 0; top: 428px; width: 100%;
    text-align: center; font-weight: 700;
    font-size: 79px; line-height: 100px; color: var(--ink);
    letter-spacing: 0.5px;
  }
  .brand-panel {
    position: absolute; left: 585px; top: 777px;
    width: 542px; height: 151px;
    background: var(--ink); border-radius: 8px;
    overflow: hidden;
  }
  .brand-dot {
    position: absolute; left: 96px; top: 12px;
    width: 96px; height: 96px; border-radius: 50%;
    background: var(--brand-orange);
  }
  .brand-name {
    position: absolute; left: 202px; top: 18px;
    color: var(--paper); font-weight: 900;
    font-size: 26px; line-height: 26px; letter-spacing: 0.5px;
  }
  .brand-web {
    position: absolute; left: 28px; top: 115px;
    color: var(--paper); font-weight: 700; font-size: 13px;
  }
  .brand-phone {
    position: absolute; left: 276px; top: 106px;
    width: 262px; height: 36px;
    display: flex; align-items: center; gap: 6px;
    padding-left: 30px;
    color: var(--paper); font-weight: 700; font-size: 17px;
  }
  .brand-phone svg.phone-bg { position: absolute; left: 0; top: 0; z-index: 0; }
  .brand-phone span, .brand-phone .phone-icon { position: relative; z-index: 1; }
  .brand-shelf {
    position: absolute; left: 0; top: 140px; width: 260px; height: 12px;
    background: var(--muted-grey); opacity: 0.8;
  }
</style>
</head>
<body>
<div class="sign">
  <svg class="tape tape--top" viewBox="0 0 1134 70" aria-hidden="true">
    <defs>
      <pattern id="hazard" width="40" height="40" patternUnits="userSpaceOnUse" patternTransform="skewX(-40)">
        <rect width="40" height="40" fill="var(--tape-gold)"/>
        <rect width="20" height="40" fill="var(--ink)"/>
      </pattern>
    </defs>
    <rect width="1134" height="70" fill="var(--tape-gold)"/>
    <rect y="0" width="1134" height="17" fill="url(#hazard)"/>
    <rect y="50" width="1134" height="20" fill="url(#hazard)"/>
    <text class="tape-text" x="0" y="40">..CAUTION........CAUTION........CAUTION........CAUTION........CAUTION........CAUTION........CAUTION........CAUTION........CAUTION..</text>
  </svg>

  <div class="headline-box"><h1 class="headline">WARNING</h1></div>

  <p class="notice">ELECTRONIC SURVEILLANCE<br>AND RECORDING DEVICES<br>INSTALLED IN THIS AREA</p>

  <div class="brand-panel">
    <div class="brand-dot"></div>
    <div class="brand-name">HARBOURLINE<br>WATCH<br>SERVICES</div>
    <div class="brand-web">WWW.HARBOURLINEWATCH.COM.AU</div>
    <div class="brand-phone">
      <svg class="phone-bg" width="262" height="36" viewBox="0 0 262 36" aria-hidden="true">
        <polygon points="16,0 262,0 246,36 0,36" fill="var(--brand-orange)"/>
        <polygon points="6,0 12,0 -4,36 -10,36" fill="var(--ink)"/>
      </svg>
      <svg class="phone-icon" width="16" height="16" viewBox="0 0 24 24" aria-hidden="true">
        <path d="M6.6 10.8a15 15 0 0 0 6.6 6.6l2.2-2.2a1 1 0 0 1 1-.25 11.4 11.4 0 0 0 3.6.57 1 1 0 0 1 1 1V20a1 1 0 0 1-1 1A17 17 0 0 1 3 4a1 1 0 0 1 1-1h3.5a1 1 0 0 1 1 1c0 1.25.2 2.45.57 3.57a1 1 0 0 1-.25 1z" fill="var(--paper)"/>
      </svg>
      <span>1300 555 014</span>
    </div>
    <div class="brand-shelf"></div>
  </div>

  <svg class="tape tape--bottom" viewBox="0 0 1134 70" aria-hidden="true">
    <rect width="1134" height="70" fill="var(--tape-gold)"/>
    <rect y="0" width="1134" height="20" fill="url(#hazard)"/>
    <rect y="52" width="1134" height="18" fill="url(#hazard)"/>
    <text class="tape-text" x="0" y="44">..CAUTION........CAUTION........CAUTION........CAUTION........CAUTION........CAUTION........CAUTION........CAUTION........CAUTION..</text>
  </svg>
</div>
</body>
</html>
```